Hi! We require a design for business cards for directors and head teachers of an international daycare for children 0 - 9. We are family-owned, -operated and -oriented. We have six locations, looking to franchise. Our USPs are: 1) Flexibility 2) Quality teachers 3) International culture 4) Best nutrition We are quality teachers and professional caretakers, but with creativity and personality! Business cards should be playful (but no Comic Sans or baby hand prints), colorful (but no rainbows), and have some breathing space. It should be obvious from the business card that we're a daycare. In 2020 we'll be launching our new website based on this design: https://plomvane.io/47K2RQLWZTD The font in the new website will be Houschka (medium, demibold, bold). We will keep our current logo, included in the files here. There are also screenshots of some designs we like. Show us your best! :)

Industry/Entity Type

Childcare

Contact Information for Business Card

Lotte de Vries-Bakhuis
Communications Wizard
Poppel Hoek International Daycare
Kastanjeweg 47 B, 2316 KR Leiden
www.poppelhoek.nl
+31 647315082

Font styles to use
Serif
Sans Serif

Colors

Designer to choose colors to be used in the design.

Requirements
Must have
• Color

```html
<!DOCTYPE html>
<html lang="en">
<head>
<meta charset="utf-8">
<title>Poppel Hoek International Daycare – Business Card</title>
<link rel="stylesheet" href="https://fonts.googleapis.com/css2?family=Montserrat:ital,wght@0,400;0,600;0,700;0,800;1,700&display=swap">
<style>
  :root {
    --backdrop: #d4c9ce;
    --paper: #ffffff;
    --cream: #f5e4c6;
    --pink: #e84a82;
    --blue: #19a3c9;
    --ink: #4a4a4a;
  }
  * { box-sizing: border-box; margin: 0; padding: 0; }
  html, body {
    width: 1200px; height: 1200px; overflow: hidden;
    background: var(--backdrop);
    font-family: "Montserrat", sans-serif;
  }
  .card {
    position: absolute;
    background: var(--paper);
  }
  .card--front { left: 257px; top: 122px; width: 695px; height: 413px; }
  .card--back  { left: 258px; top: 620px; width: 697px; height: 418px; }

  .front-panel {
    position: absolute; left: 21px; top: 21px; width: 652px; height: 372px;
    background: var(--cream);
    display: flex; align-items: center; justify-content: center;
  }
  .brand-name {
    display: flex; align-items: center; gap: 14px;
    color: var(--pink); font-weight: 800; letter-spacing: 0.5px;
  }
  .brand-name__dot { border-radius: 50%; background: var(--pink); flex: none; }
  .front-panel .brand-name { font-size: 52px; }
  .front-panel .brand-name__dot { width: 30px; height: 30px; }

  .contact { position: absolute; left: 78px; top: 113px; }
  .contact__name { color: var(--blue); font-weight: 700; font-size: 17px; letter-spacing: 0.3px; }
  .contact__role { color: var(--blue); font-weight: 400; font-size: 13.5px; margin-top: 1px; }
  .contact__list { list-style: none; margin-top: 28px; }
  .contact__item { display: flex; align-items: flex-start; font-size: 12.5px; color: var(--ink); line-height: 18px; margin-bottom: 7px; letter-spacing: 0.3px; }
  .contact__icon { width: 16px; height: 16px; margin-right: 22px; flex: none; margin-top: 1px; }
  .contact__item--address { margin-top: 8px; }

  .divider { position: absolute; left: 369px; top: 135px; width: 2px; height: 149px; background: var(--pink); }

  .card--back .brand-name { position: absolute; left: 398px; top: 170px; font-size: 28px; }
  .card--back .brand-name__dot { width: 18px; height: 18px; }

  .wave { position: absolute; left: 0; top: 0; }
  .band-text {
    position: absolute; left: 21px; width: 654px; top: 358px;
    text-align: center; color: #fff; font-weight: 700; font-style: italic;
    font-size: 19px; letter-spacing: 0.3px;
  }
</style>
</head>
<body>
  <section class="card card--front">
    <div class="front-panel">
      <div class="brand-name"><span class="brand-name__dot"></span>Poppel Hoek</div>
    </div>
  </section>

  <section class="card card--back">
    <div class="contact">
      <p class="contact__name">LOTTE DE VRIES-BAKHUIS</p>
      <p class="contact__role">Communications Wizard</p>
      <ul class="contact__list">
        <li class="contact__item">
          <svg class="contact__icon" viewBox="0 0 16 16"><circle cx="8" cy="8" r="8" fill="var(--pink)"/><path d="M5.3 4.2l1.4-.2.8 2-1 .8c.5 1.1 1.3 1.9 2.4 2.4l.8-1 2 .8-.2 1.4c-.2.5-.7.8-1.3.7C7.5 10.7 5.3 8.5 4.6 5.5c-.1-.6.2-1.1.7-1.3z" fill="#fff"/></svg>
          <span>+31 647315082</span>
        </li>
        <li class="contact__item">
          <svg class="contact__icon" viewBox="0 0 16 16"><circle cx="8" cy="8" r="8" fill="var(--pink)"/><g fill="none" stroke="#fff" stroke-width="0.8"><circle cx="8" cy="8" r="4"/><ellipse cx="8" cy="8" rx="1.8" ry="4"/><path d="M4 8h8M4.6 6h6.8M4.6 10h6.8"/></g></svg>
          <span>www.poppelhoek.nl</span>
        </li>
        <li class="contact__item contact__item--address">
          <svg class="contact__icon" viewBox="0 0 16 16"><circle cx="8" cy="8" r="8" fill="var(--pink)"/><path d="M8 3.5a3 3 0 0 1 3 3c0 2.2-3 5.8-3 5.8S5 8.7 5 6.5a3 3 0 0 1 3-3z" fill="#fff"/><circle cx="8" cy="6.5" r="1.1" fill="var(--pink)"/></svg>
          <span>Poppel Hoek International Daycare<br>Kastanjeweg 47 B, 2316 KR Leiden</span>
        </li>
      </ul>
    </div>

    <div class="divider"></div>

    <div class="brand-name"><span class="brand-name__dot"></span>Poppel Hoek</div>

    <svg class="wave" width="697" height="418" viewBox="0 0 697 418" aria-hidden="true">
      <path d="M21,358 C120,325 250,312 375,318 C480,318 600,300 675,262 L675,397 L21,397 Z" fill="var(--blue)"/>
      <path d="M21,364 C120,333 250,322 375,326 C480,326 600,308 675,276 L675,397 L21,397 Z" fill="var(--cream)"/>
      <path d="M21,370 C120,340 250,330 375,333 C480,332 600,316 675,284 L675,397 L21,397 Z" fill="var(--pink)"/>
    </svg>
    <p class="band-text">POPPEL HOEK INTERNATIONAL DAYCARE</p>
  </section>
</body>
</html>
```